Veterinary Hospital Brochure - 2 Drafts - 1 Normal and 1 Fun.

Meadowbrook Pet Hospital needs a brochure to promote our veterinary hospital. These will be delivered to local mailboxes. I would like to see atleast 2 submissions from each designer.
One submission conservative and A4 folded DL and another submission more radical and interesting with innovative folding or crazy concepts. Maybe the brochure could be designed to fold into a dog house ?
I want at least one version to be VERY SIMPLE AND INTIMATE.
Our existing website is here: http://furlane.example/ and our new website will look like this: http://trial4.pagemint.example/#home
Please use colors and images from the new website, and information from the old website. The heading font used in the new site is Qorvatype - Otter Tilt Sketchline
I want the brochure to be simple and engaging on first view, and then provide the opportunity to find more information if desired. The brochure needs to be captivating on the outside so people don't throw it away immediately.

We will soon need letterhead, flags, pens, business cards, signs and vouchers so there is the opportunity for more work for the successful designer.

Target Market(s)

Women 25 to 44

Industry/Entity Type

Veterinary

Contact Information for Business Card

Meadowbrook Pet Hospital
14 Marlow Crescent
Tamsworth Vale
NSW 2417
Phone: 02 61938205
Emergency: 0417360592
Fax: 02 83159462
www.meadowbrookvets.example
contact@meadowbrookvets.example

Font styles to use
Script

Requirements
Must have
• Colors from the new website: http://meadowbrookvets.example/ and new logo.
• Information from the old website: http://furlane.example/
• 2 drafts - A normal A4 folded DL flyer and an interesting crazy design.
Nice to have
• VERY SIMPLE
• Subdued
• Intimate
Should not have
• Intense colours
• Red

```html
<!DOCTYPE html>
<html lang="en">
<head>
<meta charset="utf-8">
<title>Meadowbrook Pet Hospital – Trifold Brochure</title>
<link rel="stylesheet" href="https://fonts.googleapis.com/css2?family=Montserrat:wght@400;500;600;700;800&display=swap">
<style>
  :root{
    --orange:#f08a4b;
    --green:#6f9c4c;
    --charcoal:#3b3430;
    --cream:#f8f1ea;
    --ink:#4a413b;
    --page:#ececec;
    --white:#ffffff;
  }
  *{box-sizing:border-box;margin:0;padding:0}
  html,body{width:1200px;height:900px;overflow:hidden;background:var(--page)}
  body{font-family:"Montserrat",sans-serif;color:var(--ink);position:relative}

  .spread{position:absolute;top:242px;width:588px;height:416px;background:var(--cream);overflow:hidden;box-shadow:0 2px 10px rgba(0,0,0,.12)}
  .spread--outside{left:8px}
  .spread--inside{left:604px}
  .shapes{position:absolute;inset:0;width:588px;height:416px;z-index:1}
  .photo{position:absolute;z-index:0}
  .panel{position:absolute;top:0;width:196px;height:416px;z-index:2}
  .panel--1{left:0}.panel--2{left:196px}.panel--3{left:392px}
  .fold{position:absolute;top:0;width:1px;height:416px;background:rgba(0,0,0,.06);z-index:3}

  /* outside */
  .intro{position:absolute;top:6px;left:14px;width:168px;color:var(--white);font-size:5.4px;line-height:1.35;text-align:center}
  .aims-title{position:absolute;top:48px;width:100%;text-align:center;color:var(--green);font-weight:700;font-size:7px;text-decoration:underline}
  .aims{position:absolute;top:60px;left:14px;width:172px;list-style:none;font-size:5.6px;line-height:1.35}
  .services-title{position:absolute;top:104px;width:100%;text-align:center;color:var(--green);font-weight:800;font-size:14px}
  .services{position:absolute;top:126px;left:14px;width:172px;display:flex;gap:8px}
  .services ul{list-style:none;flex:1;font-size:5.2px;line-height:1.45}

  .bullets li{position:relative;padding-left:7px}
  .bullets li::before{content:"";position:absolute;left:0;top:1.6px;width:3.5px;height:3.5px;background:var(--orange)}

  .contact{position:absolute;top:290px;left:0;width:196px;text-align:center;font-size:6px;line-height:1.4;color:var(--ink)}
  .contact-name{font-weight:700;font-size:9.5px;text-decoration:underline;color:var(--charcoal);margin-bottom:2px}

  .brand{position:absolute;top:18px;right:10px;font-weight:800;font-size:8.5px;color:var(--charcoal);letter-spacing:.3px}
  .cover-title{position:absolute;top:278px;left:12px;width:176px;color:var(--white);font-weight:800;line-height:1}
  .cover-title .line1{display:block;font-size:19.5px}
  .cover-title .line2{display:block;font-size:15px;margin-top:1px}
  .cover-rule{position:absolute;top:316px;left:12px;width:172px;height:1.2px;background:var(--white)}
  .cover-sub{position:absolute;top:320px;left:12px;width:174px;color:var(--white);font-weight:700;font-size:4.8px;line-height:1.35;text-align:center}

  /* inside */
  .column{position:absolute;left:12px;width:172px;font-size:6px;line-height:1.35}
  .column p{text-align:justify;margin-bottom:3px}
  .label{display:inline-block;background:var(--charcoal);color:var(--white);font-weight:700;font-size:11px;line-height:1;padding:2px 6px 3px;margin:2px 0 4px}
  .listing{display:inline-block;background:var(--green);color:var(--white);font-weight:700;font-size:6.4px;line-height:1;padding:2px 4px;margin:3px 0 2px}
  .topics{list-style:none;margin:1px 0 4px}
  .care{display:flex;gap:10px;list-style:none}
  .care ul{list-style:none;flex:1}
</style>
</head>
<body>

<!-- OUTSIDE -->
<section class="spread spread--outside" aria-label="Brochure outside">
  <div class="photo" style="left:196px;top:0;width:196px;height:264px;background:linear-gradient(160deg,#4a3d33 0%,#2e2622 60%,#241e1b 100%)" role="img" aria-label="Dark close-up photo of a cat"></div>
  <div class="photo" style="left:392px;top:0;width:196px;height:250px;background:linear-gradient(135deg,#8fb8b0 0%,#c9a77f 45%,#6a5440 100%)" role="img" aria-label="Photo of a woman hugging her dog"></div>

  <svg class="shapes" viewBox="0 0 588 416" aria-hidden="true">
    <rect x="0" y="0" width="196" height="42" fill="var(--charcoal)"/>
    <polygon points="0,296 196,326 196,338 0,308" fill="var(--green)"/>
    <polygon points="0,308 196,338 196,346 0,316" fill="var(--charcoal)"/>
    <polygon points="0,316 196,346 196,416 0,416" fill="var(--orange)"/>

    <polygon points="196,240 294,196 392,236 392,248 294,208 196,252" fill="var(--green)"/>
    <polygon points="196,252 294,208 392,248 392,256 294,216 196,260" fill="var(--charcoal)"/>
    <polygon points="196,260 294,216 392,256 392,416 196,416" fill="var(--cream)"/>

    <polygon points="392,200 490,234 588,200 588,212 490,246 392,212" fill="var(--green)"/>
    <polygon points="392,212 490,246 588,212 588,220 490,254 392,220" fill="var(--charcoal)"/>
    <polygon points="392,220 490,254 588,220 588,416 392,416" fill="var(--orange)"/>
  </svg>

  <div class="panel panel--1">
    <p class="intro">Meadowbrook Pet Hospital is a Companion Animal Veterinary Hospital in Tamsworth Vale committed to providing excellent care for loved pets and their owners.</p>
    <p class="aims-title">To Achieve This We:</p>
    <ul class="aims bullets">
      <li>Provide a welcoming environment.</li>
      <li>Treat all patients and owners as important.</li>
      <li>Educate owners to help prevent illness.</li>
      <li>When illness occurs, treat with the latest equipment and techniques.</li>
    </ul>
    <h2 class="services-title">Services</h2>
    <div class="services">
      <ul class="bullets">
        <li>Puppy Pre-School</li><li>Vaccinations</li><li>Vaccination Reminders</li><li>Companion Animal De-sexing</li><li>Emergency Surgery</li><li>Dental</li><li>Caesarian</li><li>Behaviour Consults</li><li>Grooming Support</li>
      </ul>
      <ul class="bullets">
        <li>Aged Care Consults</li><li>Nutrition Advice</li><li>Flea Treatments</li><li>Radiology</li><li>Ultrasound</li><li>Routine Blood Tests</li><li>Orthopaedic Surgery</li><li>Cruciate Repair</li><li>Skin Treatments</li>
      </ul>
    </div>
  </div>

  <div class="panel panel--2">
    <address class="contact" style="font-style:normal">
      <p class="contact-name">Meadowbrook Pet Hospital</p>
      <p>14 Marlow Crescent, Tamsworth Vale, NSW 2417</p>
      <p>Phone: 02 61938205 &nbsp;|&nbsp; Fax: 02 83159462</p>
      <p>Email: contact@meadowbrookvets.example</p>
      <p>www.meadowbrookvets.example</p>
    </address>
  </div>

  <div class="panel panel--3">
    <p class="brand">MEADOWBROOK PET HOSPITAL</p>
    <h1 class="cover-title"><span class="line1">MEADOWBROOK</span><span class="line2">PET HOSPITAL</span></h1>
    <div class="cover-rule"></div>
    <p class="cover-sub">Meadowbrook Pet Hospital is a Companion Animal Veterinary Hospital in Tamsworth Vale committed to providing excellent care for loved pets and their owners.</p>
  </div>

  <div class="fold" style="left:196px"></div>
  <div class="fold" style="left:392px"></div>
</section>

<!-- INSIDE -->
<section class="spread spread--inside" aria-label="Brochure inside">
  <div class="photo" style="left:0;top:0;width:196px;height:416px;background:linear-gradient(180deg,#efe2d4 0%,#e6d3c1 100%)" role="img" aria-label="Faint photo of a puppy sitting on a rug"></div>
  <div class="photo" style="left:196px;top:0;width:196px;height:416px;background:linear-gradient(180deg,#f1e6da 0%,#e8d8c8 100%)" role="img" aria-label="Faint warm-toned background photo"></div>
  <div class="photo" style="left:392px;top:160px;width:196px;height:256px;background:linear-gradient(135deg,#c9b39a 0%,#8c7662 50%,#5a4a3e 100%)" role="img" aria-label="Photo of a tabby cat on a book beside its owner"></div>

  <svg class="shapes" viewBox="0 0 588 416" aria-hidden="true">
    <polygon points="0,0 196,0 196,78 98,50 0,78" fill="var(--orange)"/>
    <polygon points="0,78 98,50 196,78 196,86 98,58 0,86" fill="var(--charcoal)"/>
    <polygon points="0,86 98,58 196,86 196,97 98,69 0,97" fill="var(--green)"/>

    <polygon points="392,0 588,0 588,196 490,168 392,196" fill="var(--cream)"/>
    <polygon points="392,196 490,168 588,196 588,208 490,180 392,208" fill="var(--green)"/>
    <polygon points="392,208 490,180 588,208 588,216 490,188 392,216" fill="var(--charcoal)"/>
  </svg>

  <div class="panel panel--1">
    <div class="column" style="top:96px">
      <h2 class="label">Puppy School</h2>
      <p>The classes are so much fun. You will learn heaps and your puppy will have a great time socialising.</p>
      <p style="margin-bottom:0">Course topics include:</p>
      <ul class="topics bullets">
        <li>Socialisation</li><li>Health and well being</li><li>Positive reinforcement</li><li>Canine behaviour and body language</li><li>Anxiety</li><li>Common problem behaviour</li><li>Individual problem behaviour</li><li>Environmental enrichment</li><li>General obedience</li>
      </ul>
      <p>Proper socialisation and training is essential for dogs. It prevents a range of problems from anxiety to aggression. These classes are an essential first step in your puppies life and yours as a dog owner. Even if you have been before, come along each time you get a new dog to refresh your techniques and take advantage of the puppy socialisation.</p>
      <p>Below is a video of one of the classes with Priya, our head trainer, demonstrating an introduction to walking on the lead.</p>
      <h2 class="label">Pet Care</h2>
      <div class="care">
        <ul class="bullets"><li>Microchipping.</li><li>Premium Food.</li><li>Heartworming.</li><li>Socialisation.</li><li>Yearly Vaccination and Checkup.</li></ul>
        <ul class="bullets"><li>Intestinal Worming.</li><li>Sterilisation.</li><li>Flea Treatment.</li><li>Dental Care.</li><li>Environmental Enrichment.</li></ul>
      </div>
    </div>
  </div>

  <div class="panel panel--2">
    <div class="column" style="top:6px">
      <h2 class="label">Groomers</h2>
      <p>We do not have standard grooming facilities so we try to link you with locals. If your pet requires sedation for grooming we will be happy to help. Contact us if you want to be on this page.</p>
      <h3 class="listing">Corinne in The Willow Nook - 0400813529</h3>
      <p>Corinne is a former Vet Nurse so understands animal welfare and health. She starts with a bath and can do style cuts. Everyone so far reports that Corinne does a wonderful job and is kind and patient with the animals.</p>
      <h3 class="listing">Marisol - 0400627184</h3>
      <p>Mobile. Gentle. Good with anxious dogs.</p>
      <h3 class="listing">Odette's Every Dog Grooming - 0400395716</h3>
      <p>We hear Odette Pryce is very nice with the animals and does a great job. Works from Fernhill Pet Motel which is a great place. You can find Odette on Chatterbook here: Odette Pryce. The after pictures of the dogs look very cute !</p>
      <h3 class="listing">Brackenridge Grooming Salon - 0400548263</h3>
      <p>Huge range of services. Brackenridge Grooming Salon.</p>
      <h2 class="label">Boarding</h2><br>
      <h3 class="listing">Fernhill Pet Motel - 02 40001872</h3>
      <p>Good things: We have been there and the facilities are exactly what you want from a good boarding facility. Clean, spacious, room to exercise, kind staff, welcoming atmosphere, hiding places for cats. It is a great place.</p>
      <p>Bad things: Need to book well in advance, especially for holiday periods. I suggest a year in advance for christmas.</p>
    </div>
  </div>

  <div class="panel panel--3">
    <div class="column" style="top:4px">
      <h3 class="listing">Riverbend Pet Motel - 02 40007394</h3>
      <p>Good things: Leonie and Priya went for a visit in 2015. The facilities are awesome. Very clean and well maintained. A large range or options for cats. Good facilities for dogs.</p>
      <p>Bad things: A bit of a drive.</p>
      <h3 class="listing">Ashgrove Boarding Kennels - 02 40002615</h3>
      <p>Good things: We have not heard much. Please leave a comment on Chatterbook and I will update.</p>
      <h2 class="label">Positions Vacant</h2>
      <p>There are no positions vacant at the moment, but we are always on the look out for hard working people dedicated to helping peoples lives by improving relationships with pets and pet health. If you think you have something to offer, and want a rewarding career working with great people and pets, please drop in a resume.</p>
    </div>
  </div>

  <div class="fold" style="left:196px"></div>
  <div class="fold" style="left:392px"></div>
</section>

</body>
</html>
```